Business Cards and Stationery for Mechanical Contractor
Steadfast Piping Contractors, Inc.
Business Cards and Stationery for Mechanical Contractor - Construction
Creative Brief
Professional
Warren Pickett
President
3148 Foundry Ave. Halvorsen Mills, NE 46971
wpickett@steadfastpipingco.com
www.SteadfastPipingCo.com

```html
<!DOCTYPE html>
<html lang="en">
<head>
<meta charset="utf-8">
<title>Steadfast Piping Contractors, Inc. – Business Cards</title>
<link href="https://fonts.googleapis.com/css2?family=Montserrat:wght@600;700;800&family=Open+Sans:wght@400;600&display=swap" rel="stylesheet">
<style>
  :root {
    --brand-green: #2a9142;
    --brand-green-dark: #1f7a35;
    --ink: #1a1a1a;
    --paper: #ffffff;
    --paper-shade: #eeeeee;
    --text-grey: #444444;
    --backdrop: #e6e2da;
  }
  * { box-sizing: border-box; margin: 0; padding: 0; }
  html, body { width: 1200px; height: 800px; overflow: hidden; }
  body {
    background: var(--backdrop);
    position: relative;
    font-family: "Open Sans", Arial, sans-serif;
  }
  .card {
    position: absolute;
    width: 540px;
    height: 310px;
    border-radius: 22px;
    overflow: hidden;
    box-shadow: 0 10px 28px rgba(0,0,0,0.22);
  }
  .card--front { left: 60px; top: 90px; background: var(--brand-green); }
  .card--back { left: 600px; top: 400px; background: var(--paper); }

  .card__pattern { position: absolute; inset: 0; }
  .card--front .card__pattern {
    background: linear-gradient(135deg, #2f9a48 0%, var(--brand-green) 55%, var(--brand-green-dark) 100%);
  }
  .card--back .card__pattern {
    background: linear-gradient(135deg, #fafafa 0%, var(--paper-shade) 100%);
  }

  .brand { position: absolute; font-family: "Montserrat", Arial, sans-serif; font-weight: 800; text-transform: uppercase; letter-spacing: 0.5px; line-height: 1.05; }
  .brand__rule { display: block; height: 2px; background: var(--ink); margin-top: 8px; }

  .card--front .brand { left: 0; right: 0; top: 104px; text-align: center; color: var(--paper); font-size: 25px; }
  .card--front .brand__rule { width: 300px; margin-left: auto; margin-right: auto; }
  .front__web {
    position: absolute; left: 0; right: 0; top: 200px; text-align: center;
    color: var(--paper); font-size: 15px; font-weight: 600;
  }

  .card--back .brand { left: 30px; top: 120px; width: 230px; color: var(--brand-green); font-size: 19px; }
  .card--back .brand__rule { width: 210px; }

  .person { position: absolute; right: 40px; top: 28px; text-align: right; }
  .person__name { font-family: "Montserrat", Arial, sans-serif; font-weight: 700; font-size: 19px; color: var(--brand-green); }
  .person__title { font-size: 12px; color: var(--text-grey); }

  .contact { position: absolute; right: 40px; top: 100px; list-style: none; text-align: right; }
  .contact__item { display: flex; justify-content: flex-end; align-items: center; gap: 8px; font-size: 12px; line-height: 19px; color: var(--text-grey); }
  .contact__icon { width: 13px; height: 13px; flex: none; }
  .contact__spacer { width: 13px; flex: none; }

  .card__band { position: absolute; inset: 0; }
</style>
</head>
<body>

<section class="card card--front" aria-label="Business card front">
  <div class="card__pattern" role="img" aria-label="Repeating faint brand monogram pattern in green tones"></div>
  <div class="brand">Steadfast Piping<br>Contractors, Inc.<span class="brand__rule"></span></div>
  <p class="front__web">www.SteadfastPipingCo.com</p>
</section>

<section class="card card--back" aria-label="Business card back">
  <div class="card__pattern" role="img" aria-label="Repeating faint brand monogram pattern in light grey"></div>
  <svg class="card__band" viewBox="0 0 540 310" preserveAspectRatio="none" aria-hidden="true">
    <path d="M0 272 H400 C440 272 450 240 490 240 H540 V310 H0 Z" fill="var(--brand-green)"/>
    <path d="M518 0 H540 V240 H492 C505 240 518 232 518 220 Z" fill="var(--ink)"/>
  </svg>

  <div class="brand">Steadfast Piping<br>Contractors, Inc.<span class="brand__rule"></span></div>

  <div class="person">
    <p class="person__name">Warren Pickett</p>
    <p class="person__title">President</p>
  </div>

  <ul class="contact">
    <li class="contact__item">3148 Foundry Ave.
      <svg class="contact__icon" viewBox="0 0 14 14"><circle cx="7" cy="7" r="7" fill="var(--brand-green)"/><path d="M7 3.2a2.4 2.4 0 0 1 2.4 2.4C9.4 7.6 7 10.6 7 10.6S4.6 7.6 4.6 5.6A2.4 2.4 0 0 1 7 3.2z" fill="#fff"/></svg></li>
    <li class="contact__item">Halvorsen Mills, NE 46971<span class="contact__spacer"></span></li>
    <li class="contact__item">555-214-0142
      <svg class="contact__icon" viewBox="0 0 14 14"><circle cx="7" cy="7" r="7" fill="var(--brand-green)"/><path d="M4.5 3.5l1.5 0 .6 1.8-.9.7a5 5 0 0 0 2.3 2.3l.7-.9 1.8.6v1.5c0 .4-.4.7-.8.7A6 6 0 0 1 3.8 4.3c0-.4.3-.8.7-.8z" fill="#fff"/></svg></li>
    <li class="contact__item">555-214-0187
      <svg class="contact__icon" viewBox="0 0 14 14"><circle cx="7" cy="7" r="7" fill="var(--brand-green)"/><rect x="4" y="4" width="6" height="6" fill="none" stroke="#fff" stroke-width="1"/></svg></li>
    <li class="contact__item">wpickett@steadfastpipingco.com
      <svg class="contact__icon" viewBox="0 0 14 14"><circle cx="7" cy="7" r="7" fill="var(--brand-green)"/><rect x="3.5" y="4.5" width="7" height="5" fill="none" stroke="#fff" stroke-width="1"/><path d="M3.5 4.5 7 7.3l3.5-2.8" fill="none" stroke="#fff" stroke-width="1"/></svg></li>
    <li class="contact__item">www.SteadfastPipingCo.com
      <svg class="contact__icon" viewBox="0 0 14 14"><circle cx="7" cy="7" r="7" fill="var(--brand-green)"/><circle cx="7" cy="7" r="3.5" fill="none" stroke="#fff" stroke-width="1"/><path d="M3.5 7h7M7 3.5v7" stroke="#fff" stroke-width="0.8"/></svg></li>
  </ul>
</section>

</body>
</html>
```